Calm Fern Healthcare- Aged Care and Community Services

Looking for brochure to advertise our services. I will attach a draft that we do not want to use. Looking for graphics that are as natural as possible to present a personalised service. We supply services to aged people and people with disability. Please make it look classy and professional at the same time. I am looking for creativity. I have also attached the logo. Site addresses can be the last page. ideally looking for 2 designs, one A4 and another smaller possibly DL. Looking for creative out of the box thinkers. Thank you.

Target Market(s)

Aged Care service providers, disability service providers and private hospitals

Font styles to use
Serif
Sans Serif
Script

Colors
6b449b
886aae
eea4c8
f59195
fac994
3176b5
0555a3
cedeed
e4daeb

Requirements
Must have
• Targeted imagery, content and contact details
Nice to have
• personal profiles of people happy with our services

```html
<!DOCTYPE html>
<html lang="en">
<head>
<meta charset="utf-8">
<title>Calm Fern Healthcare – Brochure</title>
<link rel="stylesheet" href="https://fonts.googleapis.com/css2?family=Montserrat:wght@300;400;600;700;800&family=Open+Sans:wght@400;600;700&display=swap">
<style>
  :root{
    --purple:#6b449b;
    --lavender:#886aae;
    --pink:#e0457f;
    --rose:#eea4c8;
    --salmon:#f59195;
    --peach:#fac994;
    --blue:#3176b5;
    --navy:#0555a3;
    --sky:#cedeed;
    --mist:#e4daeb;
    --wave:#8fb0da;
    --paper:#ffffff;
    --stage:#eceef1;
    --ink:#4a4f5c;
    --muted:#7a8090;
  }
  *{box-sizing:border-box;margin:0;padding:0}
  html,body{width:1200px;height:3000px;overflow:hidden}
  body{background:var(--stage);font-family:"Open Sans",Arial,sans-serif;color:var(--ink);position:relative}

  .spread{position:absolute;left:40px;width:1120px;height:792px;background:var(--paper);box-shadow:0 6px 24px rgba(40,50,80,.12);overflow:hidden}
  .spread--outside{top:520px}
  .spread--inside{top:1560px}
  .spread__art{position:absolute;inset:0;width:1120px;height:792px}
  .panel{position:absolute;top:0;width:560px;height:792px}
  .panel--left{left:0}
  .panel--right{left:560px}

  .brand{display:flex;align-items:center;gap:8px;font-family:"Montserrat",Arial,sans-serif;font-weight:700;color:var(--purple)}
  .brand__dot{width:12px;height:12px;border-radius:50%;background:var(--purple)}
  .brand--small{position:absolute;left:40px;top:34px;font-size:11px}
  .brand--cover{position:absolute;left:0;right:0;top:300px;justify-content:center;font-size:17px}

  .heading{font-family:"Montserrat",Arial,sans-serif;font-weight:700;letter-spacing:.06em;text-transform:uppercase;font-size:12px}
  .heading--pink{color:var(--pink)}
  .heading--purple{color:var(--purple)}
  .heading--white{color:#fff}
  .copy{font-size:9.5px;line-height:1.55;color:var(--muted)}
  .copy--white{color:#fff}

  .vision{position:absolute;left:96px;top:72px;width:330px}
  .vision .copy{margin-top:8px}

  .talk{position:absolute;left:40px;top:560px;width:300px;color:#fff}
  .talk .heading{margin-bottom:12px}
  .talk__row{display:flex;align-items:center;gap:8px;font-size:9.5px;margin-bottom:7px}
  .talk__icon{width:14px;height:14px;border-radius:50%;background:#fff;display:flex;align-items:center;justify-content:center}
  .talk__icon svg{width:8px;height:8px}

  .cover-title{position:absolute;left:0;right:0;top:356px;text-align:center;font-family:"Montserrat",Arial,sans-serif}
  .cover-title__top{display:block;font-weight:300;font-size:34px;letter-spacing:.04em;color:var(--pink);text-transform:uppercase}
  .cover-title__main{display:block;font-weight:800;font-size:52px;letter-spacing:.02em;color:var(--purple);text-transform:uppercase;line-height:1}
  .cover-title__rule{display:block;width:190px;height:4px;background:var(--pink);margin:10px auto 0}
  .cover-contact{position:absolute;left:150px;top:488px;font-family:"Montserrat",Arial,sans-serif;color:var(--purple)}
  .cover-contact__phone{display:flex;align-items:center;gap:8px;font-weight:700;font-size:17px}
  .cover-contact__mail{display:flex;align-items:center;gap:8px;font-size:10px;margin-top:6px;color:var(--muted)}
  .cover-contact svg{width:14px;height:14px}

  .about{position:absolute;left:280px;top:40px;width:250px}
  .about .copy{margin-top:8px}

  .services{position:absolute;left:40px;top:300px;width:490px}
  .services__grid{display:grid;grid-template-columns:repeat(3,1fr);gap:10px 14px;margin-top:12px}
  .service{display:flex;align-items:center;gap:7px;font-size:9px;color:var(--ink)}
  .service__icon{flex:none;width:18px;height:18px;border-radius:4px;background:var(--salmon);display:flex;align-items:center;justify-content:center}
  .service__icon svg{width:10px;height:10px}

  .believe{position:absolute;left:40px;top:440px;width:490px}
  .believe .copy{margin-top:6px}
  .start{position:absolute;left:40px;top:530px;width:490px}
  .start .copy{margin-top:6px}

  .care-band{position:absolute;left:40px;top:640px;width:480px;display:grid;grid-template-columns:1fr 1fr;gap:24px}
  .care-band .copy{margin-top:5px}

  .benefits{position:absolute;left:40px;top:40px;width:480px}
  .benefit{display:flex;gap:12px;margin-top:13px}
  .benefit__icon{flex:none;width:28px;height:28px;border-radius:50%;background:var(--mist);display:flex;align-items:center;justify-content:center}
  .benefit__icon svg{width:14px;height:14px}
  .benefit__title{font-family:"Montserrat",Arial,sans-serif;font-weight:700;font-size:9.5px;color:var(--purple);text-transform:uppercase;letter-spacing:.04em}
  .benefit .copy{margin-top:2px}

  .section{position:absolute;left:40px;width:480px}
  .section .copy{margin-top:6px}
  .section--roi{top:392px}
  .section--experience{top:478px}
  .section--empower{top:548px}
</style>
</head>
<body>

<!-- Outside spread: back panel + front cover -->
<section class="spread spread--outside">
  <svg class="spread__art" viewBox="0 0 1120 792" aria-hidden="false">
    <defs>
      <linearGradient id="photoCover" x1="0" y1="0" x2="1" y2="1">
        <stop offset="0" stop-color="#7d9a5c"/>
        <stop offset=".5" stop-color="#c9b59c"/>
        <stop offset="1" stop-color="#5a7fb5"/>
      </linearGradient>
      <linearGradient id="photoCircle" x1="0" y1="0" x2="1" y2="1">
        <stop offset="0" stop-color="#d8a98a"/>
        <stop offset="1" stop-color="#6a8fc0"/>
      </linearGradient>
    </defs>
    <!-- back panel -->
    <rect x="0" y="0" width="560" height="792" fill="#e9eff8"/>
    <path d="M0 0 H300 C200 160 420 380 560 420 V0 Z" fill="#f4f7fc"/>
    <path d="M0 520 C180 470 360 560 560 470 V792 H0 Z" fill="var(--wave)"/>
    <path d="M0 600 C200 560 380 640 560 590 V792 H0 Z" fill="#7ba0d2"/>
    <!-- front panel -->
    <rect x="560" y="0" width="560" height="792" fill="#f7f9fd"/>
    <path d="M560 0 H760 C700 160 640 420 560 560 Z" fill="#e6edf7"/>
    <path role="img" aria-label="Photo: carer and elderly man sharing a high five outdoors" d="M770 0 H1120 V290 H860 C800 220 770 120 770 0 Z" fill="url(#photoCover)"/>
    <path d="M770 0 C770 120 800 220 860 290" fill="none" stroke="var(--lavender)" stroke-width="6"/>
    <circle cx="1010" cy="298" r="66" fill="#fff"/>
    <circle role="img" aria-label="Photo: carer helping an older woman with a tablet" cx="1010" cy="298" r="58" fill="url(#photoCircle)"/>
    <path d="M560 640 C740 590 900 700 1120 620 V792 H560 Z" fill="var(--sky)"/>
    <path d="M560 700 C760 660 920 740 1120 690 V792 H560 Z" fill="var(--wave)"/>
  </svg>

  <div class="panel panel--left">
    <div class="brand brand--small"><span class="brand__dot"></span>Calm Fern Healthcare</div>
    <div class="vision">
      <h2 class="heading heading--pink">The Vision</h2>
      <p class="copy">Our vision is to be the most trusted partner in care, giving every resident and client a life shaped by their own choices. We work side by side with families and providers to deliver support that feels personal, warm and respectful, and we measure success by the comfort and dignity of the people we serve every single day.</p>
    </div>
    <div class="talk">
      <h2 class="heading heading--white">Talk to us</h2>
      <div class="talk__row"><span class="talk__icon"><svg viewBox="0 0 10 10"><path d="M2 1l2 2-1 1c.6 1.2 1.6 2.2 2.8 2.8l1-1 2 2-1.3 1.2C4.5 9 1 5.5.8 2.3Z" fill="#7ba0d2"/></svg></span>(08) 5550 0147</div>
      <div class="talk__row"><span class="talk__icon"><svg viewBox="0 0 10 10"><rect x="1" y="2" width="8" height="6" fill="none" stroke="#7ba0d2" stroke-width="1.3"/><path d="M1 2l4 3 4-3" fill="none" stroke="#7ba0d2" stroke-width="1.2"/></svg></span>hello@calmfernhealthcare.example</div>
      <div class="talk__row"><span class="talk__icon"><svg viewBox="0 0 10 10"><path d="M5 9S1.8 5.6 1.8 3.8a3.2 3.2 0 0 1 6.4 0C8.2 5.6 5 9 5 9Z" fill="#7ba0d2"/></svg></span>12 Harbour Lane, Westfield WA 6000</div>
      <div class="talk__row"><span class="talk__icon"><svg viewBox="0 0 10 10"><circle cx="5" cy="5" r="3.6" fill="none" stroke="#7ba0d2" stroke-width="1.2"/><path d="M1.4 5h7.2M5 1.4c1.6 2 1.6 5.2 0 7.2M5 1.4c-1.6 2-1.6 5.2 0 7.2" fill="none" stroke="#7ba0d2" stroke-width=".8"/></svg></span>www.calmfernhealthcare.example</div>
    </div>
  </div>

  <div class="panel panel--right">
    <div class="brand brand--cover"><span class="brand__dot"></span>Calm Fern Healthcare</div>
    <h1 class="cover-title">
      <span class="cover-title__top">Reimagining</span>
      <span class="cover-title__main">Healthcare</span>
      <span class="cover-title__rule"></span>
    </h1>
    <div class="cover-contact">
      <div class="cover-contact__phone"><svg viewBox="0 0 10 10"><path d="M2 1l2 2-1 1c.6 1.2 1.6 2.2 2.8 2.8l1-1 2 2-1.3 1.2C4.5 9 1 5.5.8 2.3Z" fill="var(--purple)"/></svg>(08) 5550 0147</div>
      <div class="cover-contact__mail"><svg viewBox="0 0 10 10"><rect x="1" y="2" width="8" height="6" fill="none" stroke="var(--purple)" stroke-width="1.2"/><path d="M1 2l4 3 4-3" fill="none" stroke="var(--purple)" stroke-width="1.1"/></svg>hello@calmfernhealthcare.example</div>
    </div>
  </div>
</section>

<!-- Inside spread -->
<section class="spread spread--inside">
  <svg class="spread__art" viewBox="0 0 1120 792">
    <defs>
      <linearGradient id="photoAbout" x1="0" y1="0" x2="1" y2="1">
        <stop offset="0" stop-color="#c7b8a4"/>
        <stop offset="1" stop-color="#8e9fb8"/>
      </linearGradient>
      <linearGradient id="photoSmall" x1="0" y1="0" x2="1" y2="1">
        <stop offset="0" stop-color="#a9c4e4"/>
        <stop offset="1" stop-color="#4f7fb8"/>
      </linearGradient>
    </defs>
    <rect x="0" y="0" width="1120" height="792" fill="#fbfcfe"/>
    <rect role="img" aria-label="Photo: nurse walking with an older woman" x="0" y="20" width="260" height="250" fill="url(#photoAbout)"/>
    <rect x="260" y="20" width="300" height="250" fill="var(--salmon)"/>
    <path d="M0 610 C180 590 380 640 560 600 V792 H0 Z" fill="var(--mist)"/>
    <rect x="20" y="622" width="520" height="150" rx="10" fill="var(--lavender)"/>
    <rect x="560" y="0" width="560" height="792" fill="#f5f8fc"/>
    <path d="M560 690 C760 650 920 720 1120 670 V792 H560 Z" fill="var(--sky)"/>
    <path d="M560 730 C760 700 940 760 1120 720 V792 H560 Z" fill="var(--wave)"/>
    <circle cx="680" cy="690" r="56" fill="#fff"/>
    <circle role="img" aria-label="Photo: carer chatting with a resident" cx="680" cy="690" r="50" fill="url(#photoSmall)"/>
    <circle cx="840" cy="690" r="56" fill="#fff"/>
    <circle role="img" aria-label="Photo: medical team at work" cx="840" cy="690" r="50" fill="url(#photoSmall)"/>
    <circle cx="1000" cy="690" r="56" fill="#fff"/>
    <circle role="img" aria-label="Photo: clinician reviewing care equipment" cx="1000" cy="690" r="50" fill="url(#photoSmall)"/>
  </svg>

  <div class="panel panel--left">
    <div class="about">
      <h2 class="heading heading--white">About us</h2>
      <p class="copy copy--white">Calm Fern Healthcare is a locally owned provider of aged care and disability services. Our skilled team brings flexible, person centred support to residents, clients and partner facilities, helping people stay connected, safe and independent. We listen first, plan together and deliver care that respects each person's story.</p>
    </div>

    <div class="services">
      <h2 class="heading heading--pink">Our services</h2>
      <div class="services__grid">
        <div class="service"><span class="service__icon"><svg viewBox="0 0 10 10"><path d="M2 5l2 2 4-4" fill="none" stroke="#fff" stroke-width="1.6"/></svg></span>Aged care staffing</div>
        <div class="service"><span class="service__icon"><svg viewBox="0 0 10 10"><path d="M2 5l2 2 4-4" fill="none" stroke="#fff" stroke-width="1.6"/></svg></span>Disability support</div>
        <div class="service"><span class="service__icon"><svg viewBox="0 0 10 10"><path d="M2 5l2 2 4-4" fill="none" stroke="#fff" stroke-width="1.6"/></svg></span>Nursing services</div>
        <div class="service"><span class="service__icon"><svg viewBox="0 0 10 10"><path d="M2 5l2 2 4-4" fill="none" stroke="#fff" stroke-width="1.6"/></svg></span>Community access</div>
        <div class="service"><span class="service__icon"><svg viewBox="0 0 10 10"><path d="M2 5l2 2 4-4" fill="none" stroke="#fff" stroke-width="1.6"/></svg></span>Personal care</div>
        <div class="service"><span class="service__icon"><svg viewBox="0 0 10 10"><path d="M2 5l2 2 4-4" fill="none" stroke="#fff" stroke-width="1.6"/></svg></span>Respite care</div>
        <div class="service"><span class="service__icon"><svg viewBox="0 0 10 10"><path d="M2 5l2 2 4-4" fill="none" stroke="#fff" stroke-width="1.6"/></svg></span>Hospital support</div>
        <div class="service"><span class="service__icon"><svg viewBox="0 0 10 10"><path d="M2 5l2 2 4-4" fill="none" stroke="#fff" stroke-width="1.6"/></svg></span>Domestic assistance</div>
        <div class="service"><span class="service__icon"><svg viewBox="0 0 10 10"><path d="M2 5l2 2 4-4" fill="none" stroke="#fff" stroke-width="1.6"/></svg></span>Care coordination</div>
      </div>
    </div>

    <div class="believe">
      <h2 class="heading heading--pink">What we believe</h2>
      <p class="copy">We believe everyone deserves care that feels like home. Kindness, trust and open communication guide every shift, every visit and every partnership we build with providers.</p>
    </div>

    <div class="start">
      <h2 class="heading heading--pink">Get started with us</h2>
      <p class="copy">Call or email our friendly team to arrange a consultation. We will learn about your facility, your residents and your goals, then tailor a service plan that fits.</p>
    </div>

    <div class="care-band">
      <div>
        <h3 class="heading heading--white">Aged care</h3>
        <p class="copy copy--white">Reliable, compassionate staff who help older people live well, with dignity and choice at every stage.</p>
      </div>
      <div>
        <h3 class="heading heading--white">Disability services</h3>
        <p class="copy copy--white">Flexible support that builds skills, confidence and community connection for every participant.</p>
      </div>
    </div>
  </div>

  <div class="panel panel--right">
    <div class="benefits">
      <h2 class="heading heading--purple">Key partnership benefits</h2>
      <div class="benefit"><span class="benefit__icon"><svg viewBox="0 0 10 10"><path d="M2 5l2 2 4-4" fill="none" stroke="var(--purple)" stroke-width="1.5"/></svg></span><div><div class="benefit__title">Flexibility</div><p class="copy">Short notice shifts and long term placements, matched to the needs of your residents.</p></div></div>
      <div class="benefit"><span class="benefit__icon"><svg viewBox="0 0 10 10"><path d="M2 5l2 2 4-4" fill="none" stroke="var(--purple)" stroke-width="1.5"/></svg></span><div><div class="benefit__title">Qualified professionals</div><p class="copy">Every team member is screened, trained and supported by experienced clinical leaders.</p></div></div>
      <div class="benefit"><span class="benefit__icon"><svg viewBox="0 0 10 10"><path d="M2 5l2 2 4-4" fill="none" stroke="var(--purple)" stroke-width="1.5"/></svg></span><div><div class="benefit__title">Continuity of care</div><p class="copy">Familiar faces build trust, reduce stress and improve outcomes for the people you care for.</p></div></div>
      <div class="benefit"><span class="benefit__icon"><svg viewBox="0 0 10 10"><path d="M2 5l2 2 4-4" fill="none" stroke="var(--purple)" stroke-width="1.5"/></svg></span><div><div class="benefit__title">Quality and compliance</div><p class="copy">Our processes align with national standards so you can focus on what matters most.</p></div></div>
      <div class="benefit"><span class="benefit__icon"><svg viewBox="0 0 10 10"><path d="M2 5l2 2 4-4" fill="none" stroke="var(--purple)" stroke-width="1.5"/></svg></span><div><div class="benefit__title">Operational efficiency</div><p class="copy">Simple booking, clear reporting and one point of contact save your team valuable time.</p></div></div>
    </div>

    <div class="section section--roi">
      <h2 class="heading heading--purple">The real return on investment</h2>
      <p class="copy">Partnering with us lowers turnover and overtime costs while lifting resident satisfaction. Consistent, well trained staff mean fewer incidents, happier families and a stronger reputation for your service in the community.</p>
    </div>
    <div class="section section--experience">
      <h2 class="heading heading--purple">Personalised resident experience</h2>
      <p class="copy">Care plans are shaped around routines, interests and cultural needs, so each person feels known and valued.</p>
    </div>
    <div class="section section--empower">
      <h2 class="heading heading--purple">Empowering customers &amp; how we serve</h2>
      <p class="copy">We give clients a voice in every decision and keep families informed every step of the way.</p>
    </div>
  </div>
</section>

</body>
</html>
```